Valbrina Soletti Winery 2023 Label

We are just about to bottle our very first Napa Valley Cabernet Sauvignon and need label ideas

Target Market(s)

Cab drinkers who like Napa California Cabs

Industry/Entity Type

Wine Making

Logo Text

Valbrina Soletti 2023 Napa Estate Grown Cabernet Sauvignon

Requirements
Must have
• Winery Name, year of vintage and Napa Estate Cab
Nice to have
• If using the initials V and S use gold letters on black or red background

```html
<!DOCTYPE html>
<html lang="en">
<head>
<meta charset="utf-8">
<title>Valbrina Soletti – 2023 Napa Estate Grown Cabernet Sauvignon</title>
<link rel="stylesheet" href="https://fonts.googleapis.com/css2?family=Cinzel:wght@700&family=Kaushan+Script&display=swap">
<style>
  :root {
    --page: #ffffff;
    --parchment: #f2e5c8;
    --parchment-deep: #e6d5ad;
    --ink: #2a2520;
    --ink-soft: #6b5e4c;
  }
  * { margin: 0; padding: 0; box-sizing: border-box; }
  html, body {
    width: 810px;
    height: 1200px;
    overflow: hidden;
    background: var(--page);
  }
  .canvas {
    position: relative;
    width: 810px;
    height: 1200px;
  }
  .label {
    position: absolute;
    left: 58px;
    top: 53px;
    width: 694px;
    height: 1096px;
    background: var(--parchment);
    color: var(--ink);
  }
  .winery-name {
    position: absolute;
    left: 0;
    right: 0;
    text-align: center;
    font-family: "Kaushan Script", cursive;
    font-weight: 400;
    line-height: 1;
    font-size: 104px;
  }
  .winery-name--first { top: 80px; }
  .winery-name--second { top: 196px; }
  .estate-scene {
    position: absolute;
    left: 34px;
    top: 330px;
    width: 623px;
    height: 309px;
    display: block;
  }
  .wine-details {
    position: absolute;
    left: 0;
    right: 0;
    top: 660px;
    text-align: center;
    font-family: "Cinzel", serif;
    font-weight: 700;
    line-height: 1;
  }
  .wine-details span { display: block; }
  .vintage { font-size: 50px; margin-bottom: 10px; }
  .region { font-size: 62px; margin-bottom: 4px; }
  .estate { font-size: 54px; margin-bottom: 8px; }
  .varietal-first { font-size: 54px; margin-bottom: 6px; }
  .varietal-second { font-size: 68px; }
</style>
</head>
<body>
  <main class="canvas">
    <section class="label">
      <h1>
        <span class="winery-name winery-name--first">Valbrina</span>
        <span class="winery-name winery-name--second">Soletti</span>
      </h1>

      <svg class="estate-scene" viewBox="0 0 623 309" role="img"
           aria-label="Pen-and-ink sketch of a hilltop villa among cypress and umbrella pine trees above rolling vineyard hills">
        <defs>
          <radialGradient id="sceneTone" cx="50%" cy="50%" r="55%">
            <stop offset="0%" stop-color="var(--ink-soft)" stop-opacity="0.45"/>
            <stop offset="100%" stop-color="var(--parchment)" stop-opacity="0"/>
          </radialGradient>
        </defs>
        <rect width="623" height="309" fill="url(#sceneTone)"/>
      </svg>

      <p class="wine-details">
        <span class="vintage">- 2023 -</span>
        <span class="region">NAPA</span>
        <span class="estate">ESTATE GROWN</span>
        <span class="varietal-first">CABERNET</span>
        <span class="varietal-second">SAUVIGNON</span>
      </p>
    </section>
  </main>
</body>
</html>
```